Brivane - Business Cards for a new venture

create business card for a startup classified business dealing in construction materials, the cards need to have a professional look but modern, more serious than playful, one of the samples must include the official font (attached), please explore using the official colors in the company's logo

Target Market(s)

Energy sector

Contact Information for Business Card

Font styles to use
Other font styles liked:
• suissnord

Requirements
Must have
• corporate colors (in logo attached)
Nice to have
• Official font (in one of the samples) font is : suissnord
Should not have
• Cartoonish look

```html
<!DOCTYPE html>
<html lang="en">
<head>
<meta charset="UTF-8">
<title>Brivane Business Cards</title>
<link href="https://fonts.googleapis.com/css2?family=Open+Sans:wght@400;600;700&display=swap" rel="stylesheet">
<style>
  :root {
    --brand-blue: #0f4470;
    --brand-grey: #9b9b9b;
    --panel-edge: #b9b9b9;
    --ink: #333333;
    --paper: #ffffff;
    --backdrop: #e9e9e9;
  }
  * { margin: 0; padding: 0; box-sizing: border-box; }
  html, body {
    width: 1200px;
    height: 900px;
    overflow: hidden;
    background: var(--backdrop);
    font-family: "Open Sans", Arial, sans-serif;
  }
  .sheet {
    width: 1200px;
    height: 900px;
    display: flex;
    flex-direction: column;
    align-items: center;
    justify-content: center;
    gap: 48px;
  }
  .card {
    position: relative;
    width: 640px;
    height: 366px;
    background: var(--paper);
    overflow: hidden;
    box-shadow: 0 6px 18px rgba(0,0,0,0.18);
  }
  .card svg.card-shapes {
    position: absolute;
    inset: 0;
    width: 100%;
    height: 100%;
  }

  /* Front */
  .brand-lockup {
    position: absolute;
    left: 60px;
    top: 58px;
    display: flex;
    align-items: center;
    gap: 14px;
  }
  .brand-dot {
    width: 30px;
    height: 30px;
    border-radius: 50%;
    background: var(--brand-blue);
  }
  .brand-name {
    font-size: 40px;
    font-weight: 600;
    letter-spacing: 6px;
    text-transform: uppercase;
    color: var(--brand-grey);
  }
  .holder {
    position: absolute;
    right: 30px;
    top: 22px;
    text-align: right;
    color: var(--ink);
  }
  .holder-name { font-size: 17px; font-weight: 700; }
  .holder-role { font-size: 12px; }
  .company {
    position: absolute;
    left: 50px;
    top: 196px;
    color: var(--ink);
    font-size: 19px;
    line-height: 1.3;
  }
  .company-name { font-weight: 700; font-size: 18px; }
  .contact {
    position: absolute;
    left: 410px;
    top: 170px;
    color: var(--paper);
    font-size: 13px;
    line-height: 27px;
  }
  .contact-row { display: flex; }
  .contact-label { width: 68px; }
  .contact-sep { width: 14px; }

  /* Back */
  .card-back { background: var(--brand-blue); }
  .back-name {
    position: absolute;
    left: 0;
    right: 0;
    top: 210px;
    text-align: center;
    font-size: 64px;
    font-weight: 600;
    letter-spacing: 10px;
    text-transform: uppercase;
    color: var(--paper);
  }
</style>
</head>
<body>
<main class="sheet">

  <section class="card card-front" aria-label="Business card front">
    <svg class="card-shapes" viewBox="0 0 640 366" preserveAspectRatio="none" aria-hidden="true">
      <path d="M372 366 L372 160 Q372 122 408 112 L640 44 L640 366 Z" fill="var(--panel-edge)"/>
      <path d="M384 366 L384 166 Q384 130 418 120 L640 54 L640 262 Q604 300 622 366 Z" fill="var(--brand-blue)"/>
    </svg>

    <div class="brand-lockup">
      <span class="brand-dot"></span>
      <span class="brand-name">Brivane</span>
    </div>

    <div class="holder">
      <div class="holder-name">Card holder Name</div>
      <div class="holder-role">Designation</div>
    </div>

    <div class="company">
      <div class="company-name">Company Full Name</div>
      <div>Company Address</div>
      <div>Street, State</div>
      <div>Country.</div>
    </div>

    <div class="contact">
      <div class="contact-row"><span class="contact-label">Office</span><span class="contact-sep">:</span><span>+xxx xxxxxxxx</span></div>
      <div class="contact-row"><span class="contact-label">Mobile</span><span class="contact-sep">:</span><span>+xxx xxxxxxxx</span></div>
      <div class="contact-row"><span class="contact-label">Email</span><span class="contact-sep">:</span><span>aaaa.aaa@aaaa.com</span></div>
    </div>
  </section>

  <section class="card card-back" aria-label="Business card back">
    <svg class="card-shapes" viewBox="0 0 640 366" preserveAspectRatio="none" aria-hidden="true">
      <path d="M0 0 L330 0 Q300 30 240 60 Q120 110 0 90 Z" fill="var(--paper)"/>
      <path d="M640 0 L520 0 Q560 20 600 10 Q625 4 640 20 Z" fill="var(--paper)"/>
    </svg>
    <div class="back-name">Brivane</div>
  </section>

</main>
</body>
</html>
```